Taboun Dinner, Dessert and Drinks Menu

We need to redesign our Dinner, Desserts, and Drinks Menus.
I have attached all three menus as pdfs. I have chosen the higher payment option because its a few pages and have removed the refund option
Taboun is the most popular Lebanese Restaurant in Melbourne and is a combination of Great Quality Traditional Food and a clean warm ambiance.
Updates
The main part of the menu is the Banquets Section. We want to push our Banquets.
The main focus of the drinks is Lebanese Wines, Lebanese Beer, Lebanese Drinks. Anything Traditional
For the Coffee Menu,
We will be Adding a Chai Latte, More Flavoured Loose Leaf Teas and Removing the Stick Tea. We will also be adding 4 coffee flavour shots to our menu.
Industry/Entity Type
Restaurant
Look and feel
Each slider illustrates characteristics of the customer's brand and the style your logo design should communicate.

```html
<!DOCTYPE html>
<html lang="en">
<head>
<meta charset="utf-8">
<title>Taboun – Desserts, Coffees and Teas</title>
<link rel="stylesheet" href="https://fonts.googleapis.com/css2?family=Maven+Pro:wght@400;500;700&family=Questrial&display=swap">
<style>
  :root {
    --paper: #f4f4f4;
    --paper-edge: #e4e4e4;
    --lime: #a6c83a;
    --red: #c8202a;
    --ink: #222222;
    --text: #3a3a3a;
    --box-top: #a87d68;
    --box-bottom: #5e3c2d;
    --box-title: #f1d68a;
    --box-text: #f2e9e3;
  }
  * { margin: 0; padding: 0; box-sizing: border-box; }
  html, body { width: 874px; height: 1200px; overflow: hidden; }
  body {
    font-family: "Questrial", sans-serif;
    color: var(--text);
    background: var(--paper);
  }
  .menu {
    position: relative;
    width: 874px; height: 1200px;
    background: radial-gradient(ellipse at 50% 40%, #ffffff 0%, var(--paper) 60%, var(--paper-edge) 100%);
    overflow: hidden;
  }
  .menu__header, .menu__footer { position: absolute; left: 0; width: 874px; }
  .menu__header { top: 0; height: 140px; }
  .menu__footer { bottom: 0; height: 80px; }
  .photo { position: absolute; }
  .photo--oval { border-radius: 50%; }
  .photo--rounded { border-radius: 8px; }

  .brand {
    position: absolute; left: 612px; top: 76px; width: 216px; height: 50px;
    display: flex; align-items: center; justify-content: center; gap: 10px;
  }
  .brand__mark { width: 14px; height: 14px; background: var(--lime); }
  .brand__name {
    font-family: "Maven Pro", sans-serif;
    font-weight: 700; font-size: 40px; letter-spacing: 2px; color: var(--ink);
    line-height: 50px;
  }

  .section-title {
    position: absolute; font-family: "Maven Pro", sans-serif;
    font-weight: 500; font-size: 30px; line-height: 36px; color: var(--ink);
  }
  .item { position: absolute; }
  .item__name {
    font-family: "Maven Pro", sans-serif;
    font-weight: 700; font-size: 17px; color: var(--red); line-height: 20px; white-space: nowrap;
  }
  .item__desc {
    margin-top: 6px; font-size: 14.2px; line-height: 17px; text-align: justify;
  }
  .item__tag {
    font-size: 13px; font-weight: 700; color: #111; margin-left: 14px;
  }
  .item--featured {
    background: linear-gradient(180deg, var(--box-top), var(--box-bottom));
    border-radius: 8px;
  }
  .item--featured .item__name { color: var(--box-title); }
  .item--featured .item__desc { color: var(--box-text); }
  .list { list-style: none; margin-top: 6px; font-size: 14.5px; line-height: 20px; }

  .order-line {
    position: absolute; left: 0; top: 1144px; width: 874px; text-align: center;
    font-family: "Maven Pro", sans-serif;
    font-size: 21px; line-height: 24px; color: #222;
  }
  .order-line strong { font-weight: 700; }
</style>
</head>
<body>
<main class="menu">
  <svg class="menu__header" viewBox="0 0 874 140" aria-hidden="true">
    <defs>
      <linearGradient id="band" x1="0" x2="1">
        <stop offset="0" stop-color="#2a1c16"/>
        <stop offset="0.3" stop-color="#a8917f"/>
        <stop offset="0.55" stop-color="#3a2a22"/>
        <stop offset="0.8" stop-color="#8f7a6a"/>
        <stop offset="1" stop-color="#2a1c16"/>
      </linearGradient>
    </defs>
    <path d="M0 0 H874 V40 C700 100 500 110 300 80 C180 62 80 55 0 60 Z" fill="url(#band)"/>
    <path d="M0 60 C80 55 180 62 300 80 C480 108 620 120 874 70 L874 82 C620 132 470 120 300 92 C180 74 80 72 0 78 Z" fill="#a6c83a"/>
  </svg>

  <div class="photo photo--oval" style="left:24px;top:71px;width:279px;height:145px;background:radial-gradient(ellipse, #e6e1c8 0%, #f2f1e8 70%);" role="img" aria-label="Photo of sweet cheese pastries topped with crushed pistachio"></div>
  <div class="photo photo--oval" style="left:320px;top:99px;width:241px;height:124px;background:radial-gradient(ellipse at 40% 50%, #f4f4f0 0%, #e9b6c8 60%, #d9679a 100%);" role="img" aria-label="Photo of a cup of white coffee with a mint leaf on a floral tray"></div>

  <div class="brand">
    <span class="brand__mark"></span>
    <span class="brand__name">TABOUN</span>
  </div>

  <h2 class="section-title" style="left:56px;top:225px;">Desserts</h2>
  <h2 class="section-title" style="left:493px;top:225px;">Coffees and Teas</h2>

  <section class="item" style="left:56px;top:283px;width:355px;">
    <h3 class="item__name">Baklawa - $5.90 (3 Pieces)</h3>
    <p class="item__desc">A Middle Eastern delicacy. Baked layers of very thin filo pastry stuffed with chopped cashews and topped with homemade rose syrup.</p>
  </section>
  <section class="item" style="left:56px;top:396px;width:355px;">
    <h3 class="item__name">Namoura - $5.90 (3 Pieces)</h3>
    <p class="item__desc">Lebanese semolina cake topped with almonds and homemade syrup.</p>
  </section>
  <section class="item item--featured" style="left:38px;top:481px;width:389px;height:108px;padding:12px 16px 0 18px;">
    <h3 class="item__name">Layali Libnan (Lebanese Nights) - $6.90</h3>
    <p class="item__desc">This is a cold semolina pudding with real home distilled rosewater, topped with hand crushed pistachios, homemade cream, and syrup.</p>
  </section>
  <section class="item" style="left:56px;top:616px;width:355px;">
    <h3 class="item__name">Rahat al Halkoum - $5.90 (3 Pieces)</h3>
    <p class="item__desc">Lebanese Turkish Delights that are flavoured with rosewater or lemon and served in between traditional round Qamar biscuits.</p>
  </section>
  <section class="item" style="left:56px;top:721px;width:355px;">
    <h3 class="item__name">Halawet al Jebn - $6.90 <span class="item__tag">TABOUN FAVOURITE</span></h3>
    <p class="item__desc">A popular Lebanese dessert made from sweet cheese which is drizzled with homemade rose water syrup then topped with crushed pistachio.</p>
  </section>

  <div class="photo photo--rounded" style="left:54px;top:828px;width:199px;height:129px;background:linear-gradient(135deg,#d9c79a,#c9852f 50%,#e9dcae);" role="img" aria-label="Photo of three pieces of baklawa with pistachio"></div>
  <div class="photo photo--rounded" style="left:264px;top:828px;width:183px;height:129px;background:linear-gradient(135deg,#8c9a6a,#e8e6d8 45%,#9aa85a);" role="img" aria-label="Photo of semolina pudding with cream and crushed pistachio"></div>
  <div class="photo photo--rounded" style="left:54px;top:976px;width:173px;height:129px;background:linear-gradient(135deg,#6e6a64,#d8d4cc 50%,#a9a39a);" role="img" aria-label="Photo of Turkish delight pieces dusted with sugar"></div>
  <div class="photo photo--rounded" style="left:249px;top:976px;width:198px;height:129px;background:linear-gradient(135deg,#ffffff,#c67a35 50%,#f5f2ee);" role="img" aria-label="Photo of namoura semolina cake squares with almonds"></div>

  <section class="item item--featured" style="left:476px;top:274px;width:360px;height:130px;padding:8px 17px 0 17px;">
    <h3 class="item__name">Café Blanc - $3.00</h3>
    <p class="item__desc">Café Blanc is a sedative that calms the nerves while stimulating digestion after a particularly rich or heavy meal. Café Blanc is a soothing combination of hot water and Orange Blossom water.</p>
  </section>
  <section class="item" style="left:493px;top:430px;">
    <h3 class="item__name">Lebanese Coffee Tray&nbsp; $3.50</h3>
  </section>
  <section class="item" style="left:493px;top:466px;">
    <h3 class="item__name">Other Available Coffees&nbsp; $3.50</h3>
    <ul class="list">
      <li>Cappuccino</li><li>Café Latte</li><li>Short Macchiato</li><li>Long Macchiato</li><li>Short Black</li><li>Long Black</li><li>Flat White</li>
    </ul>
  </section>
  <div class="photo photo--rounded" style="left:651px;top:516px;width:180px;height:116px;background:linear-gradient(120deg,#5a3a12,#c8962e 40%,#f2f0ea 75%);" role="img" aria-label="Photo of coffee pouring from a brass pot into a small cup"></div>

  <section class="item" style="left:493px;top:658px;">
    <h3 class="item__name">Hot Chocolate&nbsp; $4.50</h3>
  </section>
  <section class="item" style="left:493px;top:697px;">
    <h3 class="item__name">Traditional Teas&nbsp; $3.50</h3>
    <ul class="list">
      <li>Lebanese Loose Leaf Tea</li><li>Lebanese Mint Tea</li><li>Lebanese Anise Tea</li><li>Lebanese Mountain Tea</li>
    </ul>
  </section>
  <div class="photo photo--rounded" style="left:646px;top:828px;width:182px;height:119px;background:linear-gradient(160deg,#5e2a2a,#c9c7c2 40%,#8e8a86);" role="img" aria-label="Photo of a cup of tea on a silver tray with loose leaves"></div>

  <section class="item" style="left:493px;top:937px;">
    <h3 class="item__name">Chai Latte</h3>
    <ul class="list" style="margin-top:4px;"><li>More Flavoured Loose Leaf Teas</li></ul>
  </section>
  <section class="item" style="left:493px;top:996px;">
    <h3 class="item__name">Flavoured Coffee</h3>
    <ul class="list">
      <li>Flavoured Coffee_1</li><li>Flavoured Coffee_2</li><li>Flavoured Coffee_3</li><li>Flavoured Coffee_4</li>
    </ul>
  </section>
  <div class="photo" style="left:656px;top:1002px;width:180px;height:112px;background:radial-gradient(ellipse,#e8cfa0 0%,#f6efe2 55%,#ffffff 100%);" role="img" aria-label="Photo of a chai latte in a glass with a cinnamon stick"></div>

  <svg class="menu__footer" viewBox="0 0 874 80" aria-hidden="true">
    <defs>
      <linearGradient id="bandBottom" x1="0" x2="1">
        <stop offset="0" stop-color="#2a1c16"/>
        <stop offset="0.3" stop-color="#a8917f"/>
        <stop offset="0.55" stop-color="#3a2a22"/>
        <stop offset="0.8" stop-color="#8f7a6a"/>
        <stop offset="1" stop-color="#2a1c16"/>
      </linearGradient>
      <linearGradient id="limeBand" x1="0" x2="1">
        <stop offset="0" stop-color="#a6c83a"/>
        <stop offset="0.5" stop-color="#cde27a"/>
        <stop offset="1" stop-color="#a6c83a"/>
      </linearGradient>
    </defs>
    <path d="M0 30 C250 -4 620 -4 874 30 V80 H0 Z" fill="url(#limeBand)"/>
    <path d="M0 35 C250 64 620 64 874 35 V80 H0 Z" fill="url(#bandBottom)"/>
  </svg>
  <p class="order-line">Phone or text <strong>0000 000 000</strong> to pre order</p>
</main>
</body>
</html>
```